Bref créative
Stand out Biz Cards & Stationery for Quarvenix
A Cutting Edge Consulting & Executive Coaching Firm
Simple
Torben K. Aldavisto, PhD
President & CEO
48207 E Corvane Ave
Suite 2875-417
Phoenix, AZ 85093-6718
Torben@Aldavisto-mail.test
www.Aldavisto-mail.test
It might be questionable to use the tag line in the Logo since the font is very tiny.
The significant problems we have, cannot be solved at the same level of thinking with which we created them. -- Gustav Merriwold

```html
<!DOCTYPE html>
<html lang="en">
<head>
<meta charset="utf-8">
<title>Quarvenix Stationery</title>
<link href="https://fonts.googleapis.com/css2?family=Tinos:wght@400;700&display=swap" rel="stylesheet">
<style>
  :root {
    --bg: #e9e9ea;
    --paper: #ffffff;
    --navy: #1f2f8f;
    --blue: #2f5fc8;
    --sky: #4aa3e6;
    --red: #d22a1e;
    --ink: #3a4a7a;
    --faint: #f6e4df;
  }
  * { box-sizing: border-box; margin: 0; padding: 0; }
  html, body { width: 1200px; height: 744px; overflow: hidden; }
  body { background: var(--bg); font-family: "Tinos", "Times New Roman", serif; color: var(--ink); position: relative; }
  .piece { position: absolute; background: var(--paper); overflow: hidden; }
  .brand { position: absolute; font-weight: 700; color: var(--navy); letter-spacing: 0.5px; }
  .band { position: absolute; left: 0; width: 100%; display: block; }
  .smalltext { position: absolute; font-size: 6px; line-height: 1.35; text-align: center; color: var(--ink); }
  .mark-faint { position: absolute; border-radius: 50%; background: var(--faint); opacity: 0.7; }

  .letterhead { left: 36px; top: 29px; width: 415px; height: 667px; }
  .letterhead .brand { left: 22px; top: 22px; font-size: 26px; }
  .letterhead .mark-faint { left: 250px; top: 400px; width: 160px; height: 160px; }
  .letterhead .band { bottom: 0; height: 48px; }
  .letterhead .smalltext { left: 0; right: 0; bottom: 50px; }
  .letterhead .web { position: absolute; left: 0; right: 0; bottom: 70px; text-align: center; font-size: 5.5px; }

  .envelope { left: 480px; top: 29px; width: 401px; height: 259px; }
  .envelope .brand { left: 20px; top: 26px; font-size: 22px; }
  .envelope .mark-faint { left: 290px; top: 70px; width: 100px; height: 100px; }
  .envelope .band { bottom: 0; height: 60px; }
  .envelope .smalltext { left: 0; right: 0; bottom: 62px; }

  .envelope-back { left: 480px; top: 305px; width: 401px; height: 127px; }
  .envelope-back .band { top: 0; height: 127px; }
  .envelope-back .brand { left: 0; right: 0; top: 40px; text-align: center; color: #fff; font-size: 18px; }

  .card { width: 213px; border-radius: 8px; }
  .card-front { left: 910px; top: 29px; height: 122px; }
  .card-front .brand { left: 0; right: 0; top: 8px; text-align: center; font-size: 20px; }
  .card-front .name { position: absolute; left: 0; right: 0; top: 37px; text-align: center; color: var(--red); font-size: 9px; }
  .card-front .title { position: absolute; left: 0; right: 0; top: 49px; text-align: center; font-size: 6.5px; }
  .card-front .smalltext { left: 0; right: 0; top: 62px; font-size: 5.5px; }
  .card-front .band { bottom: 0; height: 20px; }

  .card-blue { left: 910px; top: 168px; height: 110px; background: linear-gradient(180deg, var(--navy) 0%, var(--blue) 55%, var(--sky) 100%); }
  .card-blue .quote { position: absolute; left: 28px; right: 28px; top: 38px; text-align: center; font-size: 6px; line-height: 1.35; color: #fff; }
  .card-white { left: 910px; top: 298px; height: 115px; }
  .card-white .quote { position: absolute; left: 28px; right: 28px; top: 36px; text-align: center; font-size: 6px; line-height: 1.35; color: var(--navy); }
  .quote .author { color: var(--red); display: block; }
</style>
</head>
<body>

<section class="piece letterhead">
  <div class="brand">Quarvenix</div>
  <div class="mark-faint"></div>
  <div class="web">www.Aldavisto-mail.test</div>
  <p class="smalltext">48207 E Corvane Ave, Suite 2875-417, Phoenix, AZ 85093-6718<br>Torben@Aldavisto-mail.test · www.Aldavisto-mail.test</p>
  <svg class="band" viewBox="0 0 415 48" preserveAspectRatio="none" aria-hidden="true">
    <defs><linearGradient id="lhBand" x1="0" y1="0" x2="0" y2="1"><stop offset="0" stop-color="#2c3ea8"/><stop offset="1" stop-color="#4aa3e6"/></linearGradient></defs>
    <path d="M0,22 Q200,0 415,12 L415,48 L0,48 Z" fill="url(#lhBand)"/>
    <path d="M0,22 Q200,0 415,12" fill="none" stroke="#fff" stroke-width="2"/>
  </svg>
</section>

<section class="piece envelope">
  <div class="brand">Quarvenix</div>
  <div class="mark-faint"></div>
  <p class="smalltext">48207 E Corvane Ave, Suite 2875-417, Phoenix, AZ 85093-6718<br>Torben@Aldavisto-mail.test<br>www.Aldavisto-mail.test</p>
  <svg class="band" viewBox="0 0 401 60" preserveAspectRatio="none" aria-hidden="true">
    <defs><linearGradient id="envBand" x1="0" y1="0" x2="0" y2="1"><stop offset="0" stop-color="#1f2f8f"/><stop offset="1" stop-color="#4aa3e6"/></linearGradient></defs>
    <path d="M0,10 Q200,38 401,8 L401,60 L0,60 Z" fill="url(#envBand)"/>
  </svg>
</section>

<section class="piece envelope-back">
  <svg class="band" viewBox="0 0 401 127" preserveAspectRatio="none" aria-hidden="true">
    <defs><linearGradient id="flap" x1="0" y1="0" x2="0" y2="1"><stop offset="0" stop-color="#1f2f8f"/><stop offset="0.6" stop-color="#2f5fc8"/><stop offset="1" stop-color="#4aa3e6"/></linearGradient></defs>
    <path d="M0,0 L401,0 L401,22 L370,68 L31,68 L0,22 Z" fill="url(#flap)"/>
  </svg>
  <div class="brand">Quarvenix</div>
</section>

<section class="piece card card-front">
  <div class="brand">Quarvenix</div>
  <div class="name">Torben K. Aldavisto, PhD</div>
  <div class="title">President &amp; CEO</div>
  <p class="smalltext">48207 E Corvane Ave, Suite 2875-417, Phoenix, AZ 85093-6718<br>Torben@Aldavisto-mail.test<br>www.Aldavisto-mail.test</p>
  <svg class="band" viewBox="0 0 213 20" preserveAspectRatio="none" aria-hidden="true">
    <path d="M0,6 Q110,16 213,4 L213,20 L0,20 Z" fill="#dde7f5"/>
  </svg>
</section>

<section class="piece card card-blue">
  <p class="quote">The significant problems we have, cannot be solved at the same level of thinking with which we created them.<br>-- Gustav Merriwold</p>
</section>

<section class="piece card card-white">
  <p class="quote">The significant problems we have, cannot be solved at the same level of thinking with which we created them.<span class="author">-- Gustav Merriwold</span></p>
</section>

</body>
</html>
```